Design Powerpoint template for US based family office

Corvale Stewardship Group is the investment firm of a family based in the US. All of our investments have a financial return but also a social or environmental good. We care about the impact our money has on society and manage our firm to reflect those beliefs. We are in need of a powerpoint template for presentations that we give at conferences. This should incorporate our logo and be easy to print. Slides will vary and include text, charts, graphics and maps. Formatted options for each should be included in the template.

Target Market(s)

Other investors and startup entrepreneurs looking for funding. Our website is here in case it helps get a sense of our work: http://corvalestewardshipgroup.example/

Industry/Entity Type

Finance

Font styles to use
Sans Serif

Colors
0255a3
85cae6

Requirements
Must have
• Look very professional, clean lines etc. Built in graphics templates in the same color scheme are also important. Our logo should also be included on each slide in some way, page numbers are also important on all slides except the first title slide.

```html
<!DOCTYPE html>
<html lang="en">
<head>
<meta charset="utf-8">
<title>Corvale Stewardship Group – Slide Template</title>
<link rel="stylesheet" href="https://fonts.googleapis.com/css2?family=Open+Sans:wght@400;600;700&family=Montserrat:wght@400;600;700&display=swap">
<style>
  :root {
    --brand-blue: #0255a3;
    --brand-sky: #85cae6;
    --sky-soft: #a9dcef;
    --ink: #333a44;
    --muted: #6b7480;
    --page: #e9ebee;
    --white: #ffffff;
  }
  * { box-sizing: border-box; margin: 0; padding: 0; }
  html, body { width: 849px; height: 1200px; overflow: hidden; }
  body { background: var(--page); font-family: "Open Sans", Arial, sans-serif; color: var(--ink); position: relative; }

  .slide {
    position: absolute; left: 28px; width: 793px; height: 552px;
    background: var(--white); box-shadow: 0 2px 6px rgba(0,0,0,.18); overflow: hidden;
  }
  .slide--where { top: 23px; }
  .slide--chart { top: 617px; }

  .slide__header {
    position: absolute; left: 0; top: 0; width: 100%; height: 104px;
    background: var(--brand-blue); color: var(--white);
  }
  .slide__marker {
    position: absolute; left: 22px; top: 22px; width: 20px; height: 20px;
    background: var(--white); border-radius: 2px;
  }
  .slide__marker::after {
    content: ""; position: absolute; left: 5px; top: 5px; width: 10px; height: 10px; background: var(--brand-blue);
  }
  .slide__title {
    position: absolute; left: 56px; top: 10px; font-family: "Montserrat", Arial, sans-serif;
    font-weight: 600; font-size: 38px; line-height: 44px;
  }
  .slide__kicker {
    position: absolute; left: 58px; top: 64px; font-size: 11px; letter-spacing: 3px; font-weight: 600;
  }
  .brand {
    position: absolute; right: 26px; top: 20px; display: flex; align-items: center; gap: 10px;
    font-family: "Open Sans", Arial, sans-serif; font-weight: 600; font-size: 13px; letter-spacing: 1px;
    line-height: 16px; color: var(--white); text-transform: uppercase;
  }
  .brand__dot { width: 34px; height: 34px; border-radius: 50%; border: 2px solid var(--white); }

  .slide__footer {
    position: absolute; left: 0; top: 480px; width: 100%; height: 52px; background: var(--brand-blue);
    color: var(--white); font-size: 11px;
  }
  .slide__footer-note { position: absolute; left: 24px; top: 18px; }
  .slide__page {
    position: absolute; right: 22px; top: 10px; width: 34px; height: 32px; background: var(--brand-sky);
    color: var(--white); font-weight: 700; font-size: 14px; text-align: center; line-height: 32px;
  }
  .slide__strip { position: absolute; left: 0; top: 532px; width: 100%; height: 20px; background: #f3f4f6; }

  .headline {
    position: absolute; left: 0; top: 136px; width: 100%; text-align: center; font-size: 19px; color: #222;
  }
  .headline strong { font-weight: 700; font-size: 22px; }

  .steps { position: absolute; left: 18px; top: 180px; }
  .step-num { font-family: "Montserrat", Arial, sans-serif; font-weight: 600; font-size: 40px; fill: var(--white); }
  .step-label { font-size: 12px; fill: var(--white); }
  .step-label--dark { fill: #21425f; }

  .about {
    position: absolute; left: 512px; top: 188px; width: 262px; font-size: 12.5px; line-height: 19px;
    text-align: justify; color: #444;
  }

  .timeline { position: absolute; left: 0; top: 180px; width: 100%; height: 240px; }
  .timeline__rail { position: absolute; left: 60px; right: 60px; top: 54px; height: 3px; background: var(--sky-soft); }
  .holding { position: absolute; top: 8px; width: 112px; text-align: center; }
  .holding__ring {
    width: 94px; height: 94px; margin: 0 auto; border-radius: 50%; border: 4px solid var(--brand-blue);
    background: var(--white); display: flex; align-items: center; justify-content: center;
    font-weight: 700; font-size: 11px; line-height: 14px; color: #222; padding: 0 8px;
  }
  .holding__text { margin-top: 12px; font-size: 8.5px; line-height: 12px; color: var(--muted); }
</style>
</head>
<body>

<section class="slide slide--where">
  <header class="slide__header">
    <span class="slide__marker"></span>
    <h1 class="slide__title">Where we invest</h1>
    <p class="slide__kicker">IMPACT INVESTING</p>
    <div class="brand"><span class="brand__dot"></span><span>Corvale<br>Stewardship</span></div>
  </header>

  <h2 class="headline"><strong>Add some head lines here</strong> for the following diagram and explanation</h2>

  <svg class="steps" width="470" height="250" viewBox="0 0 470 250">
    <g stroke-linejoin="round">
      <polygon points="0,0 104,0 104,128 52,158 0,128" fill="#0255a3"/>
      <polygon points="188,0 292,0 292,128 240,158 188,128" fill="#0255a3"/>
      <polygon points="376,0 470,0 470,128 423,158 376,128" fill="#0255a3"/>
      <polygon points="94,60 146,90 198,60 198,196 146,226 94,196" fill="#85cae6"/>
      <polygon points="282,60 334,90 386,60 386,196 334,226 282,196" fill="#85cae6"/>
    </g>
    <text class="step-num" x="40" y="46">1</text>
    <text class="step-label" x="12" y="86">Affordable</text>
    <text class="step-label" x="12" y="102">and Green</text>
    <text class="step-label" x="12" y="118">Real Estate</text>

    <text class="step-num" x="134" y="136">2</text>
    <text class="step-label step-label--dark" x="120" y="176">Education</text>

    <text class="step-num" x="228" y="46">3</text>
    <text class="step-label" x="200" y="86">Energy &amp;</text>
    <text class="step-label" x="200" y="102">Environment</text>

    <text class="step-num" x="322" y="136">4</text>
    <text class="step-label step-label--dark" x="310" y="182">Financial</text>
    <text class="step-label step-label--dark" x="310" y="198">Inclusion</text>

    <text class="step-num" x="410" y="46">5</text>
    <text class="step-label" x="406" y="90">Health</text>
  </svg>

  <p class="about">Corvale Stewardship Group makes investments in profitable companies, nonprofit organizations and new ventures creating positive social or environmental impact. To enhance innovation, we invest using a variety of capital types, including equity, debt, and hybrid</p>

  <footer class="slide__footer">
    <span class="slide__footer-note">Copy righted to Corvale Stewardship Group</span>
    <span class="slide__page">03</span>
  </footer>
  <div class="slide__strip"></div>
</section>

<section class="slide slide--chart">
  <header class="slide__header">
    <span class="slide__marker"></span>
    <h1 class="slide__title">Our chart here</h1>
    <p class="slide__kicker">IMPACT INVESTING</p>
    <div class="brand"><span class="brand__dot"></span><span>Corvale<br>Stewardship</span></div>
  </header>

  <div class="timeline">
    <div class="timeline__rail"></div>
    <div class="holding" style="left:72px">
      <div class="holding__ring">Fixed Income</div>
      <p class="holding__text">We gain exposure to a range of strategies in fixed income, mostly through third-party managers offering steady returns.</p>
    </div>
    <div class="holding" style="left:199px">
      <div class="holding__ring">Public Equity</div>
      <p class="holding__text">We invest in publicly traded companies through third-party managers with a clear impact focus.</p>
    </div>
    <div class="holding" style="left:332px">
      <div class="holding__ring">Fixed Income</div>
      <p class="holding__text">We gain exposure to a range of strategies in fixed income, mostly through third-party managers offering steady returns.</p>
    </div>
    <div class="holding" style="left:465px">
      <div class="holding__ring">Alternative Investments</div>
      <p class="holding__text">We make investments in private assets, including venture capital and real assets.</p>
    </div>
    <div class="holding" style="left:598px">
      <div class="holding__ring">Direct Investments</div>
      <p class="holding__text">We invest directly in companies with financial and impact returns.</p>
    </div>
  </div>

  <footer class="slide__footer">
    <span class="slide__footer-note">Copy righted to Corvale Stewardship Group</span>
    <span class="slide__page">04</span>
  </footer>
  <div class="slide__strip"></div>
</section>

</body>
</html>
```